Poster Needed for Church Conference

I need a poster for a weekend conference at my church. Looking to attract as many people as possible. We are a church in the suburbs of Houston. This is mainly for our own church members but we are opening it up to outside church members.

Please see previous design from last conference and all other graphic work that can (doesn't need to be) included.

Target Market(s)

It's targeted for all people. But our main audience is families. around the age of 30 should be main target.

Industry/Entity Type

Non-Profit

Font styles to use
Serif
Sans Serif

Colors

Designer to choose colors to be used in the design.

Requirements
Must have
• 11x17 design with ability to shrink and blow up. but ideally for 11x17
• Content and wording:
• "Rooted Lantern Conference: Bridging the gap between generations and passing on our deepest beliefs and values."
• Featuring Dr. Glen Marlowe. Author of "The Map of Q9"
• Aug 25-26: Friday 8-10 pm, Saturday 4-8 pm
• Cost Adults $15/Children $5: Covers admission to all sessions and workshops, refreshments and Saturday dinner. *kids 5 and under free
• Childcare provided for all sessions. "
• Please use church logo and address on flyer: 4312 Orchard Bend, Missouri City, TX 77512
Nice to have
• Ideally it will be designed so that we can crop a 16:9 pp announcement slide and header for our website.
Should not have
• anything offensive

```html
<!DOCTYPE html>
<html lang="en">
<head>
<meta charset="utf-8">
<title>Rooted Lantern Conference</title>
<link rel="stylesheet" href="https://fonts.googleapis.com/css2?family=Bebas+Neue&family=Jost:wght@400;500&family=Shadows+Into+Light&display=swap">
<style>
  :root {
    --yellow: #f2e42c;
    --green: #a4d23a;
    --tape: rgba(233, 224, 172, 0.88);
    --tape-soft: rgba(236, 229, 190, 0.8);
    --ink: #1c1a17;
    --brand-green: #3fa64a;
    --paper: #ffffff;
  }
  html, body {
    margin: 0;
    padding: 0;
    overflow: hidden;
    background: #e9e9e9;
  }
  .poster {
    position: relative;
    width: 1200px;
    height: 777px;
    overflow: hidden;
    background: var(--green);
  }
  .backdrop {
    position: absolute;
    inset: 0;
  }
  .tape {
    position: absolute;
    background: var(--tape);
    clip-path: polygon(0 4%, 3% 0, 97% 2%, 100% 0, 99% 50%, 100% 100%, 96% 97%, 4% 100%, 0 96%, 1% 50%);
  }

  /* Featuring label */
  .featuring-tape {
    left: 48px; top: -6px;
    width: 200px; height: 124px;
    transform: rotate(-2deg);
    z-index: 3;
    background: rgba(214, 205, 160, 0.9);
  }
  .featuring-label {
    position: absolute;
    left: 76px; top: 20px;
    z-index: 4;
    font-family: "Bebas Neue", sans-serif;
    font-size: 40px;
    letter-spacing: 1px;
    color: var(--ink);
  }

  /* Speaker card */
  .speaker-card {
    position: absolute;
    margin: 0;
    left: 44px; top: 88px;
    width: 376px; height: 400px;
    background: var(--paper);
    transform: rotate(8deg);
    box-shadow: 2px 4px 10px rgba(0,0,0,0.25);
    z-index: 2;
  }
  .speaker-photo {
    position: absolute;
    left: 20px; top: 20px;
    width: 336px; height: 284px;
    background: radial-gradient(circle at 55% 45%, #b98e74 0%, #6b4c3d 32%, #111 62%);
  }
  .speaker-caption {
    position: absolute;
    left: 16px; top: 306px;
    width: 340px;
    font-family: "Shadows Into Light", cursive;
    color: var(--ink);
    line-height: 0.98;
    transform: rotate(4deg);
    transform-origin: left top;
  }
  .speaker-name { font-size: 28px; letter-spacing: 2px; text-transform: uppercase; }
  .speaker-role { font-size: 21px; padding-left: 4px; }
  .speaker-book { font-size: 26px; letter-spacing: 2px; text-transform: uppercase; }

  .book-cover {
    position: absolute;
    left: 218px; top: 522px;
    width: 166px; height: 226px;
    transform: rotate(-8deg);
    background: linear-gradient(160deg, #ffffff 0%, #e6e6e6 60%, #cfd8cf 100%);
    box-shadow: 3px 5px 10px rgba(0,0,0,0.3);
    z-index: 3;
  }

  /* Title */
  .title-tape {
    left: 420px; top: 118px;
    width: 710px; height: 220px;
    transform: rotate(-14deg);
    background: linear-gradient(180deg, var(--tape-soft) 0%, rgba(230, 238, 200, 0.75) 55%, var(--tape-soft) 100%);
  }
  .title-block {
    position: absolute;
    left: 480px; top: 100px;
    width: 640px;
    transform: rotate(-16deg);
    text-align: center;
    color: var(--ink);
  }
  .event-title {
    margin: 0;
    font-family: "Bebas Neue", sans-serif;
    font-weight: 400;
    font-size: 86px;
    line-height: 0.86;
    letter-spacing: 2px;
  }
  .event-tagline {
    margin: 14px 0 0;
    font-family: "Jost", sans-serif;
    font-weight: 500;
    font-size: 23px;
    line-height: 1.25;
  }

  /* Details */
  .details-tape {
    left: 488px; top: 382px;
    width: 664px; height: 224px;
    transform: rotate(-1deg);
  }
  .details {
    position: absolute;
    left: 556px; top: 392px;
    width: 570px;
    color: var(--ink);
    transform: rotate(-1deg);
  }
  .event-dates {
    margin: 0;
    font-family: "Bebas Neue", sans-serif;
    font-size: 49px;
    line-height: 1;
    letter-spacing: 1px;
  }
  .event-dates small { font-size: 28px; }
  .event-cost {
    margin: 10px 0 0;
    font-family: "Shadows Into Light", cursive;
    font-size: 27px;
    line-height: 30px;
    letter-spacing: 1.6px;
  }
  .event-cost .caps { text-transform: uppercase; letter-spacing: 2.4px; }
  .childcare {
    margin: 2px 0 0 124px;
    font-family: "Shadows Into Light", cursive;
    font-size: 19px;
    letter-spacing: 1px;
  }

  /* Church */
  .church-tape {
    left: 592px; top: 634px;
    width: 476px; height: 134px;
  }
  .church {
    position: absolute;
    left: 592px; top: 664px;
    width: 476px;
    text-align: center;
  }
  .church-name {
    display: flex;
    align-items: center;
    justify-content: center;
    gap: 10px;
    margin: 0;
    font-family: "Jost", sans-serif;
    font-weight: 500;
    font-size: 28px;
    color: var(--brand-green);
  }
  .church-dot {
    width: 22px; height: 22px;
    border-radius: 50%;
    background: var(--brand-green);
  }
  .church-address {
    margin: 24px 0 0;
    font-family: "Jost", sans-serif;
    font-weight: 500;
    font-size: 15px;
    color: var(--ink);
  }
</style>
</head>
<body>
<main class="poster">
  <svg class="backdrop" width="1200" height="777" viewBox="0 0 1200 777" aria-hidden="true">
    <rect width="1200" height="777" fill="var(--green)"/>
    <polygon points="0,0 1200,0 1200,136 0,356" fill="var(--yellow)"/>
  </svg>

  <div class="tape featuring-tape"></div>
  <div class="featuring-label">Featuring:</div>

  <figure class="speaker-card">
    <div class="speaker-photo" role="img" aria-label="Portrait photograph of the speaker on a dark stage background"></div>
    <figcaption class="speaker-caption">
      <div class="speaker-name">Dr. Glen Marlowe</div>
      <div class="speaker-role">Author of</div>
      <div class="speaker-book">“The Map of Q9”</div>
    </figcaption>
  </figure>

  <div class="book-cover" role="img" aria-label="Cover of the book The Map of Q9 by Glen Marlowe"></div>

  <div class="tape title-tape"></div>
  <header class="title-block">
    <h1 class="event-title">Rooted Lantern<br>Conference:</h1>
    <p class="event-tagline">“Bridging the gap between generations<br>and passing on our deepest beliefs and values.”</p>
  </header>

  <div class="tape details-tape"></div>
  <section class="details">
    <p class="event-dates">Aug 25–26: Fri 8–10<small>PM</small>, Sat 4–8<small>PM</small></p>
    <p class="event-cost"><span class="caps">Cost: Adults $15 / Children $5:</span><br>Covers admission to all sessions and<br>workshops, refreshments and Saturday<br>dinner. *Kids 5 and under free*</p>
    <p class="childcare">Childcare provided for all sessions.</p>
  </section>

  <div class="tape church-tape"></div>
  <footer class="church">
    <p class="church-name"><span class="church-dot"></span>Cedar Hollow Community Church</p>
    <p class="church-address">4312 Orchard Bend, Missouri City, TX 77512</p>
  </footer>
</main>
</body>
</html>
```